Staff Assisted Hemodialysis Company Need a fantastic website

Our Company name is: Bellmont Home Renal Partners, we offer a valuable service to renal patients, who cannot dialyze in-center. BHRP sends a licensed nurse to the patient's home, to perform the lifesaving procedure of hemodialysis. Our clinic, which will also perform in-center hemodialysis, offers CKD training as well as a support group where guest speakers, patients, and anyone who wishes to attend can share their experiences. We are the 1st ESRD clinic in Arkansas to offer these services. We would like links to different patient resources (recipes) , as well as a prospective patient interactive form that is HIPAA compliant. We would also like a tab where prospective employees can view our job openings. We would also like to have a map of our location, the qualifications of our staffs, a listing of our affiliations.

Target Market(s)

ESRD patients; people with end stage renal disease, hypertension, or diabetes
people looking to learn about dialysis or kidney failure

Industry/Entity Type

It Company

Number of Pages Required

4 page

Font styles to use
Serif

Colors
a64599
e667a6
f59296
85acd3
85cae6

Requirements
Must have
• Our tagline: " The 1st Staff Assissted Hemodialysis Provider in the State of Arkansas"
• A patient resources tab these can include links to:
• http://www.dialcircle27.example/QRT.php
• http://mirvaleunion.example/
• http://www.hpx-agency.example/Center/Special-Topic/End-Stage-Renal-Disease-ESRD-Center.html
• https://www.nephrolink.example/
• http://www.cystwatch.example/
• We would like a tab listing our Affiliations:
• Tollbridge Business Guild
• VOTE - members of
• LMCS- members of

```html
<!DOCTYPE html>
<html lang="en">
<head>
<meta charset="utf-8">
<title>Bellmont Home Renal Partners</title>
<link rel="stylesheet" href="https://fonts.googleapis.com/css2?family=Raleway:wght@400;500;600;700&family=Oswald:wght@400;500&display=swap">
<style>
:root{
  --plum:#a64599;
  --pink:#e667a6;
  --coral:#f59296;
  --sky:#85acd3;
  --aqua:#85cae6;
  --ink:#333333;
  --muted:#666666;
  --line:#dddddd;
  --panel:#e9e9e9;
  --band:#4a4a4a;
}
*{box-sizing:border-box;margin:0;padding:0}
html,body{width:1200px;height:2609px;overflow:hidden;background:#fff}
body{position:relative;font-family:'Raleway',sans-serif;color:var(--ink)}
.abs{position:absolute}

/* header */
.topbar{left:0;top:0;width:1200px;height:6px;display:flex}
.topbar span{flex:1}
.site-header{left:0;top:6px;width:1200px;height:84px;background:#fff}
.brand{left:75px;top:22px;display:flex;align-items:center;gap:12px}
.brand-mark{width:40px;height:40px;border-radius:50%;background:var(--plum)}
.brand-name{font-size:22px;font-weight:600;color:var(--plum)}
.main-nav{right:60px;top:0;height:84px;display:flex;gap:0}
.main-nav a{display:block;padding:0 21px;line-height:84px;font-size:15px;color:var(--ink);text-decoration:none;position:relative}
.main-nav a.active::after{content:"";position:absolute;left:14px;right:14px;bottom:0;height:5px;background:var(--plum)}

/* hero */
.hero{left:0;top:90px;width:1200px;height:490px;background:linear-gradient(90deg,#eaf3f8 0%,#dceaf2 30%,#c7dbe6 60%,#b5cedc 100%)}
.hero-photo{left:90px;top:0;width:420px;height:490px;background:linear-gradient(180deg,#e6d5cb 0%,#dcc3b6 35%,#bfdde8 70%,#8fc2d8 100%);opacity:.75}
.hero-copy{left:545px;top:235px;width:500px;text-align:center}
.hero-copy .l1{font-size:42px;font-weight:400;color:#222;line-height:1.2;white-space:nowrap}
.hero-copy .l2{margin:10px 0;padding:10px 0;border-top:2px solid #333;border-bottom:2px solid #333;font-family:'Oswald',sans-serif;font-size:50px;font-weight:500;color:var(--plum);line-height:1.15;white-space:nowrap}
.hero-copy .l3{font-size:42px;color:#222;line-height:1.2;white-space:nowrap}
.slide-arrow{top:300px}

/* appointment */
.appointment{left:75px;top:580px;width:1050px;height:226px;background:var(--plum);color:#fff}
.appointment h2{position:absolute;left:28px;top:22px;font-size:30px;font-weight:500}
.appointment .fold{position:absolute;right:0;top:0;width:0;height:0;border-top:40px solid #fff;border-left:40px solid var(--pink)}
.field{position:absolute;display:flex;align-items:center;font-size:13px}
.field label{width:95px}
.field .input{height:30px;background:#fff}

/* features */
.feature{top:900px;width:328px;height:215px;text-align:center;padding-top:30px}
.feature.highlight{background:var(--panel)}
.feature h3{font-size:24px;font-weight:700;margin:14px 0 22px;color:#222}
.feature.highlight h3{font-weight:500}
.feature p{font-size:12px;line-height:1.6;color:#444;padding:0 50px}

/* band */
.welcome-band{left:0;top:1180px;width:1200px;height:255px;background:linear-gradient(90deg,#3d3d3d 0%,#575757 30%,#4a4a4a 70%,#5e5e5e 100%)}
.welcome-band h2{position:absolute;left:0;width:1200px;top:130px;text-align:center;color:#fff;font-size:38px;font-weight:400}
.welcome-band h2 b{font-weight:700}

/* team */
.section-title{left:0;width:1200px;top:1485px;text-align:center;font-size:40px;font-weight:400;color:#222}
.member{top:1557px;width:244px;height:415px;border:1px solid var(--line);background:#fff}
.member .photo{width:242px;height:272px}
.member h4{text-align:center;font-size:18px;font-weight:700;margin:26px 0 12px}
.member p{font-size:12px;line-height:1.6;color:#444;text-align:center;padding:0 22px}

/* testimonials / news */
.lower{left:0;top:2036px;width:1200px;height:377px;background:var(--panel)}
.lower h3{font-size:22px;font-weight:600;color:var(--plum)}
.quote-photo{left:78px;top:2150px;width:140px;height:140px;border-radius:50%;background:linear-gradient(160deg,#cfe6ef 0%,#9fc9d9 55%,#e8d3c8 100%);border:4px solid #fff}
.quote-name{left:78px;top:2310px;width:140px;text-align:center;font-size:16px;font-weight:700}
.quote-date{left:78px;top:2335px;width:140px;text-align:center;font-size:13px;color:#444}
.quote-text{left:252px;top:2150px;width:340px;font-size:13px;line-height:1.55;color:#444}
.quote-text p+p{margin-top:16px}
.news{left:612px;top:2090px;width:515px;height:288px;border:2px solid #fff;padding:20px 24px}
.news h3{color:var(--pink)}
.news-item{font-size:13px;line-height:1.55;color:#444;margin-top:14px}
.news-item time{display:block;text-align:right;margin-top:8px;color:#333}

/* footer */
.footer-links{left:0;top:2478px;width:1200px;display:flex;justify-content:center;gap:62px}
.footer-link{display:flex;align-items:center;gap:14px;font-size:14px;line-height:1.3;color:#444}
.footer-link b{font-weight:700;color:#333}
.footer-link .ico{width:38px;height:38px;flex:none}
.copyright{left:0;top:2555px;width:1200px;text-align:center;font-size:12px;color:#333}
</style>
</head>
<body>

<div class="abs topbar">
  <span style="background:var(--plum)"></span><span style="background:var(--pink)"></span><span style="background:var(--coral)"></span><span style="background:var(--sky)"></span><span style="background:var(--aqua)"></span><span style="background:var(--plum)"></span>
</div>

<header class="abs site-header">
  <div class="abs brand"><span class="brand-mark"></span><span class="brand-name">Bellmont Home Renal Partners</span></div>
  <nav class="abs main-nav">
    <a class="active" href="#">Home</a><a href="#">Services</a><a href="#">Patients</a><a href="#">Professionals</a><a href="#">Patient Resources</a><a href="#">Events</a>
  </nav>
</header>

<section class="abs hero">
  <div class="abs hero-photo" role="img" aria-label="Smiling nurse with a stethoscope in a bright clinic"></div>
</section>
<div class="abs hero-copy">
  <div class="l1">The 1st Staff Assissted</div>
  <div class="l2">HEMODIALYSIS PROVIDER</div>
  <div class="l3">in the State of Arkansas</div>
</div>
<svg class="abs slide-arrow" style="left:0" width="50" height="70" viewBox="0 0 50 70"><polyline points="44,4 6,35 44,66" fill="none" stroke="#fff" stroke-width="3"/></svg>
<svg class="abs slide-arrow" style="right:0" width="50" height="70" viewBox="0 0 50 70"><polyline points="6,4 44,35 6,66" fill="none" stroke="#fff" stroke-width="3"/></svg>

<section class="abs appointment">
  <span class="fold"></span>
  <h2>Appointments for Hemodialysis</h2>
  <div class="field" style="left:55px;top:87px"><label>First Name</label><span class="input" style="width:350px"></span></div>
  <div class="field" style="left:550px;top:87px"><label>Last Name</label><span class="input" style="width:350px"></span></div>
  <div class="field" style="left:55px;top:132px"><label>Contact No.</label><span class="input" style="width:350px"></span></div>
  <div class="field" style="left:550px;top:132px"><label>Address</label><span class="input" style="width:350px"></span></div>
  <div class="field" style="left:55px;top:177px"><label>Patient Detail</label><span class="input" style="width:845px"></span></div>
</section>

<div class="abs feature" style="left:100px">
  <svg width="40" height="36" viewBox="0 0 40 36"><rect x="2" y="8" width="36" height="26" rx="3" fill="var(--plum)"/><rect x="13" y="2" width="14" height="8" rx="2" fill="none" stroke="var(--plum)" stroke-width="3"/><path d="M17 14h6v5h5v6h-5v5h-6v-5h-5v-6h5z" fill="#fff"/></svg>
  <h3>24/7 Availability</h3>
  <p>Trained nurses stay on call around the clock, with gentle home visits and steady support for every patient.</p>
</div>
<div class="abs feature highlight" style="left:435px">
  <svg width="44" height="38" viewBox="0 0 44 38"><path d="M22 36 4 18C-2 10 4 1 12 2c5 0 8 4 10 7 2-3 5-7 10-7 8-1 14 8 8 16z" fill="var(--plum)"/><polyline points="6,19 15,19 19,11 24,26 28,17 38,17" fill="none" stroke="#fff" stroke-width="2.5"/></svg>
  <h3>Home Base Care</h3>
  <p>A licensed nurse comes to your home and performs each session with care, comfort and clear guidance.</p>
</div>
<div class="abs feature" style="left:770px">
  <svg width="36" height="38" viewBox="0 0 36 38"><circle cx="18" cy="9" r="7" fill="var(--sky)"/><path d="M3 37c0-11 6-18 15-18s15 7 15 18z" fill="var(--sky)"/><path d="M16 24h4v3h3v4h-3v3h-4v-3h-3v-4h3z" fill="#fff"/></svg>
  <h3>Professionals</h3>
  <p>Qualified renal staff with years of training bring skill, patience and kindness to every single visit.</p>
</div>

<section class="abs welcome-band" role="img" aria-label="Soft darkened photo of a nurse in a clinic">
  <h2>First Time in <b>ARKANSAS</b></h2>
</section>

<h2 class="abs section-title">Meet With Our Team</h2>
<article class="abs member" style="left:75px"><div class="photo" role="img" aria-label="Team member portrait, nurse with stethoscope" style="background:linear-gradient(180deg,#f1f1f1,#dcd6d2 50%,#8ec5d6)"></div><h4>Lerem Ipsum</h4><p>Licensed renal nurse caring for patients at home with skill, patience and a warm word.</p></article>
<article class="abs member" style="left:343px"><div class="photo" role="img" aria-label="Team member portrait, nurse in surgical cap" style="background:linear-gradient(180deg,#d9dde2,#e3d2c6 50%,#7fbfd3)"></div><h4>Lerem Ipsum</h4><p>Dialysis technician who keeps every machine safe, clean and ready for the next visit.</p></article>
<article class="abs member" style="left:612px"><div class="photo" role="img" aria-label="Team member portrait, nurse in scrubs" style="background:linear-gradient(180deg,#cfdbe4,#d8c4b8 50%,#86aed0)"></div><h4>Lerem Ipsum</h4><p>Care coordinator who plans schedules, answers calls and guides new families each week.</p></article>
<article class="abs member" style="left:881px"><div class="photo" role="img" aria-label="Team member portrait, doctor in white coat" style="background:linear-gradient(180deg,#f2f2f2,#e6d0bf 50%,#eef0f2)"></div><h4>Lerem Ipsum</h4><p>Staff physician who reviews treatment plans and supports the nurses in the field.</p></article>

<section class="abs lower">
  <h3 class="abs" style="left:75px;top:54px">Testimonials &amp; Clients</h3>
</section>
<div class="abs quote-photo" role="img" aria-label="Patient receiving care from a nurse"></div>
<div class="abs quote-name">Lorem Ipsum</div>
<div class="abs quote-date">04/13/2015</div>
<svg class="abs" style="left:84px;top:2338px" width="10" height="14" viewBox="0 0 10 14"><polygon points="9,1 1,7 9,13" fill="#222"/></svg>
<svg class="abs" style="left:202px;top:2338px" width="10" height="14" viewBox="0 0 10 14"><polygon points="1,1 9,7 1,13" fill="#222"/></svg>
<div class="abs quote-text">
  <p>Our nurse arrives on time, explains every step and makes long sessions feel calm. Dialysis at home gave our family its evenings back.</p>
  <p>The staff answered every call and stayed patient with all our questions from the very first week.</p>
</div>
<div class="abs news">
  <h3>Events &amp; News</h3>
  <div class="news-item">Support group meets this month with a guest speaker sharing kidney-friendly recipes and tips for life on dialysis.<time>04/28/2015</time></div>
  <div class="news-item">New CKD training classes open at our clinic for patients, families and anyone who wants to learn more.<time>04/28/2015</time></div>
</div>

<div class="abs footer-links">
  <div class="footer-link"><svg class="ico" viewBox="0 0 38 38"><path d="M8 2h16l8 8v26H8z" fill="none" stroke="var(--plum)" stroke-width="2.5"/><path d="M24 2v8h8" fill="none" stroke="var(--plum)" stroke-width="2.5"/><line x1="13" y1="20" x2="27" y2="20" stroke="var(--plum)" stroke-width="2"/><line x1="13" y1="27" x2="27" y2="27" stroke="var(--plum)" stroke-width="2"/></svg><span>Download<br><b>Patient Forms</b></span></div>
  <div class="footer-link"><svg class="ico" viewBox="0 0 38 38"><rect x="3" y="3" width="32" height="32" rx="4" fill="var(--pink)"/></svg><span>Watch us on<br><b>Streamly</b></span></div>
  <div class="footer-link"><svg class="ico" viewBox="0 0 38 38"><rect x="3" y="3" width="32" height="32" rx="4" fill="var(--sky)"/></svg><span>Like us on<br><b>Friendwall</b></span></div>
  <div class="footer-link"><svg class="ico" viewBox="0 0 38 38"><circle cx="19" cy="19" r="16" fill="var(--aqua)"/></svg><span>Follow us on<br><b>Chirpline</b></span></div>
</div>
<p class="abs copyright">© 2015 Bellmont Home Renal Partners, Inc. All rights reserved</p>

</body>
</html>
```